Electronic Time-sheet & Training Tracker for Mobile phone

App should have two functions:Access by Quillon and Vextora:Employee Tracker: I need to be able to add/edit employees and personal information (example: address, DL number, SS number, DOB, employee number), drug screen information (type DCCHA and expiration date, DCCFO and expiration date, DCCHT and expiration date, PRAV Background and expiration date) and enter multiple training records (KEMB8 and expiration date). It would be great to receive an expiration alert.The employee would only have visibility to his own. Supervisors would have overall visibility.Time-Sheet:I need a time-sheet that can be accessed on the phone, be completed, then have the ability to electronically sign and submitted. The timesheet needs to be used two-fold for supervision to verify hours and edit (if need be), he would approve and forward to payroll. The time-sheet should be daily or weekly if we can get the data to fit. We are trying to streamline field supervisors having to log on to a computer to access a server just to do time-sheets. We need it to be user-friendly. We need to have two places to have electronic signatures (employee and supervisor).
A couple of designers have asked for an additional day. Others are making changes based on feedback.
Industrial (Oil ad Gas)
- Timesheet portion may require multiple entries with billable, non-billable, shop drop-down and job number and category code (LRS, HTS, FMS, ITP, OBS, HTT, NDE)
- Tracker - Training expiration alert or notifications by email to employee and supervisors.

```html
<!DOCTYPE html>
<html lang="en">
<head>
<meta charset="utf-8">
<title>Field Crew App – Profile, Training Stats and Timesheet Screens</title>
<link rel="stylesheet" href="https://fonts.googleapis.com/css2?family=Poppins:wght@400;500;600&display=swap">
<style>
  :root{
    --blue:#1f6fe5;
    --blue-soft:#e8f0fd;
    --ink:#1d2433;
    --muted:#8a93a5;
    --line:#e6e9ef;
    --band:#f1f3f7;
    --red:#f25b5b;
    --green:#35c47a;
    --bg:#ffffff;
    --avatar:#c9d3e2;
  }
  *{box-sizing:border-box;margin:0;padding:0}
  html,body{width:1200px;height:675px;overflow:hidden}
  body{background:var(--bg);font-family:"Poppins",sans-serif;color:var(--ink);position:relative}

  .screen{position:absolute;top:14px;width:292px;height:548px;background:#fff;border-radius:28px;
    box-shadow:0 6px 26px rgba(31,60,120,.14);overflow:hidden}
  .screen--about{left:110px}
  .screen--training{left:478px}
  .screen--timesheet{left:846px}

  .caption{position:absolute;top:596px;width:292px;text-align:center;font-size:13px;line-height:20px;color:#3a4150}
  .caption--about{left:110px}.caption--training{left:478px}.caption--timesheet{left:846px}

  .app-bar{height:78px;display:flex;align-items:flex-end;padding:0 18px 16px;position:relative;border-bottom:1px solid var(--line)}
  .app-bar__title{position:absolute;left:0;right:0;bottom:16px;text-align:center;font-size:13px;font-weight:500}
  .back{width:16px;height:16px}

  .profile-head{display:flex;align-items:center;padding:14px 18px 10px}
  .avatar{width:42px;height:42px;border-radius:50%;background:linear-gradient(135deg,#d8dfeb,#a9b6c9);flex:none}
  .profile-head__text{margin-left:12px;flex:1}
  .profile-head__name{font-size:14px;font-weight:500}
  .profile-head__role{font-size:9px;color:var(--muted)}
  .edit{width:13px;height:13px}

  .tabs{display:flex;margin:4px 18px 10px;border:1.5px solid var(--blue);border-radius:6px;overflow:hidden}
  .tab{flex:1;text-align:center;font-size:10px;padding:6px 0;color:var(--ink)}
  .tab--active{background:var(--blue);color:#fff}

  .section-head{display:flex;justify-content:space-between;align-items:center;padding:8px 18px 6px;font-size:11px;font-weight:500}
  .row{display:flex;justify-content:space-between;align-items:flex-start;padding:7px 18px;border-bottom:1px solid var(--line);font-size:11px}
  .row__value{font-size:8.5px;color:var(--blue);text-align:right;max-width:120px;line-height:13px}
  .band{height:10px;background:var(--band);margin-top:6px}

  .toggle{width:26px;height:12px;border-radius:6px;background:var(--green);position:relative}
  .toggle::after{content:"";position:absolute;right:2px;top:2px;width:8px;height:8px;border-radius:50%;background:#fff}

  .alert{margin:22px 18px 0;background:var(--red);color:#fff;border-radius:6px;text-align:center;padding:11px 6px 9px}
  .alert__title{font-size:11px;font-weight:500}
  .alert__note{font-size:7.5px;opacity:.9}

  .form{padding:14px 18px 0}
  .form__heading{font-size:11px;font-weight:500;margin-bottom:10px}
  .field{display:flex;justify-content:space-between;align-items:center;height:24px;border:1px solid #b9c8e6;border-radius:12px;padding:0 10px;margin-bottom:9px;font-size:8.5px;color:var(--muted)}
  .field svg{width:11px;height:11px}
  .attachments{border-top:8px solid var(--band);padding:12px 18px 0}
  .file{display:flex;justify-content:space-between;align-items:center;font-size:8.5px;color:var(--blue);margin:8px 0 16px}
  .file__remove{color:var(--red);font-size:11px}
  .upload{display:flex;align-items:center;justify-content:center;gap:6px;width:84px;height:24px;margin:0 auto;border:1.5px solid var(--blue);border-radius:12px;font-size:9px;color:var(--blue)}
  .upload svg{width:10px;height:10px}
  .add-btn{position:absolute;left:62px;right:62px;bottom:30px;height:28px;border-radius:14px;background:var(--blue);color:#fff;font-size:10px;font-weight:500;display:flex;align-items:center;justify-content:center}
</style>
</head>
<body>

<!-- Screen 1: profile, about tab -->
<section class="screen screen--about">
  <header class="app-bar">
    <svg class="back" viewBox="0 0 16 16"><path d="M10 3 5 8l5 5" fill="none" stroke="#1d2433" stroke-width="1.6"/></svg>
    <h1 class="app-bar__title">Dane's Profile</h1>
  </header>
  <div class="profile-head">
    <div class="avatar" role="img" aria-label="Employee profile photo"></div>
    <div class="profile-head__text">
      <div class="profile-head__name">Dane Holloway</div>
      <div class="profile-head__role">Site Engineer</div>
    </div>
    <svg class="edit" viewBox="0 0 14 14"><path d="M2 12l1-3 7-7 2 2-7 7z" fill="none" stroke="#1d2433" stroke-width="1.2"/></svg>
  </div>
  <nav class="tabs"><span class="tab tab--active">About</span><span class="tab">Training Stats</span></nav>
  <div class="section-head">Basic Info
    <svg class="edit" viewBox="0 0 14 14"><path d="M2 12l1-3 7-7 2 2-7 7z" fill="none" stroke="#1f6fe5" stroke-width="1.2"/></svg></div>
  <div class="row"><span>Full Name</span><span class="row__value">Dane Marcus Holloway</span></div>
  <div class="row"><span>Email</span><span class="row__value">dane.h@corvalmail.net</span></div>
  <div class="row"><span>Phone</span><span class="row__value">+1 555 014 2290</span></div>
  <div class="row"><span>DOB</span><span class="row__value">15 - Nov - 1988</span></div>
  <div class="row"><span>Address</span><span class="row__value">82 Fernhill Lane,<br>Ridgeport, TX</span></div>
  <div class="band"></div>
  <div class="section-head">License &amp; Employment
    <svg class="edit" viewBox="0 0 14 14"><path d="M2 12l1-3 7-7 2 2-7 7z" fill="none" stroke="#1f6fe5" stroke-width="1.2"/></svg></div>
  <div class="row"><span>DL Number</span><span class="row__value">C3-458-202</span></div>
  <div class="row"><span>SS Number</span><span class="row__value">0981-34-2367</span></div>
  <div class="row"><span>Designation</span><span class="row__value">Site Engineer</span></div>
</section>

<!-- Screen 2: training stats -->
<section class="screen screen--training">
  <header class="app-bar">
    <svg class="back" viewBox="0 0 16 16"><path d="M10 3 5 8l5 5" fill="none" stroke="#1d2433" stroke-width="1.6"/></svg>
    <h1 class="app-bar__title">Dane's Profile</h1>
  </header>
  <div class="profile-head">
    <div class="avatar" role="img" aria-label="Employee profile photo"></div>
    <div class="profile-head__text"><div class="profile-head__name">Dane Holloway</div></div>
  </div>
  <nav class="tabs"><span class="tab">About</span><span class="tab tab--active">Training Stats</span></nav>
  <div class="section-head">Course Details <span class="toggle"></span></div>
  <div class="row"><span>Name</span><span class="row__value">GSW12</span></div>
  <div class="row"><span>Code</span><span class="row__value">12345678</span></div>
  <div class="row"><span>Desc.</span><span class="row__value">Gas leak response and field safety basics</span></div>
  <div class="row"><span>Joined On</span><span class="row__value">05 - Nov - 2019</span></div>
  <div class="row"><span>Expiry</span><span class="row__value">15 - Nov - 2019</span></div>
  <div class="alert">
    <div class="alert__title">Your Course is Expiring Soon!</div>
    <div class="alert__note">Renew within 5 days</div>
  </div>
</section>

<!-- Screen 3: add timesheet -->
<section class="screen screen--timesheet">
  <header class="app-bar">
    <svg class="back" viewBox="0 0 16 16"><path d="M10 3 5 8l5 5" fill="none" stroke="#1d2433" stroke-width="1.6"/></svg>
    <h1 class="app-bar__title">Add New Timesheet</h1>
  </header>
  <div class="form">
    <h2 class="form__heading">Project Details</h2>
    <div class="field">Project name</div>
    <div class="field">Description</div>
    <div class="field">Date
      <svg viewBox="0 0 12 12"><rect x="1.5" y="2.5" width="9" height="8" rx="1" fill="none" stroke="#1f6fe5"/><path d="M1.5 5h9M4 1v3M8 1v3" stroke="#1f6fe5"/></svg></div>
    <div class="field">Starting Time
      <svg viewBox="0 0 12 12"><circle cx="6" cy="6" r="4.6" fill="none" stroke="#1f6fe5"/><path d="M6 3.5V6l1.8 1.2" fill="none" stroke="#1f6fe5"/></svg></div>
    <div class="field">Ending Time
      <svg viewBox="0 0 12 12"><circle cx="6" cy="6" r="4.6" fill="none" stroke="#1f6fe5"/><path d="M6 3.5V6l1.8 1.2" fill="none" stroke="#1f6fe5"/></svg></div>
  </div>
  <div class="attachments">
    <h2 class="form__heading">Attachments</h2>
    <div class="file"><span>IF_04 - Dec - 2019</span><span class="file__remove">✕</span></div>
    <div class="upload">
      <svg viewBox="0 0 10 10"><path d="M5 8V2M2.5 4.5 5 2l2.5 2.5" fill="none" stroke="#1f6fe5" stroke-width="1.2"/></svg>Upload</div>
  </div>
  <div class="add-btn">ADD</div>
</section>

<p class="caption caption--about">Viewing Employee Profile<br>- About Tab</p>
<p class="caption caption--training">Viewing Employee Profile<br>- Training Stats</p>
<p class="caption caption--timesheet">Adding new Timesheet</p>

</body>
</html>
```